Brightmoor Partners Branding Revamp

We are a consulting company, looking for a way to display and promote our brand. We have 2 sides to the business- Brightmoor (financial) and Partners (cyber security). The financial side products relate to business necessities: card processing, website design/hosting/maintenance, VoIP phone systems. The cyber security side promotes a bundled package of 4 solutions: network vulnerability scan, dark web scan, anti-ransomeware/malware software, and image-level backups. We want people to understand that partnering with Brightmoor Partners gives them “Elevated Peace of Mind” (tagline). Current badge and logos uploaded.

Target Market(s)

Small businesses

Contact Information for Business Card

Lena Marwick, Vice President, lena@brightmoorpartners.example, 555-806-1937, www.brightmoorpartners.example

Requirements
Nice to have
• I do prefer the darker background for front and back

```html
<!DOCTYPE html>
<html lang="en">
<head>
<meta charset="utf-8">
<title>Brightmoor Partners – Business Card</title>
<link href="https://fonts.googleapis.com/css2?family=Montserrat:wght@300;400;600;700;800&family=Open+Sans:wght@400;600&display=swap" rel="stylesheet">
<style>
  :root {
    --backdrop: #e9eaea;
    --paper: #ffffff;
    --red: #c1272d;
    --red-deep: #8e1217;
    --red-bright: #e8262c;
    --ink: #1a1a1a;
    --band-light: rgba(255, 255, 255, 0.22);
  }
  * { margin: 0; padding: 0; box-sizing: border-box; }
  html, body {
    width: 852px; height: 1200px; overflow: hidden;
    background: radial-gradient(ellipse at 50% 45%, #f7f7f7 0%, var(--backdrop) 75%);
    font-family: "Open Sans", Arial, sans-serif;
  }
  .stage { position: relative; width: 852px; height: 1200px; }

  .card {
    position: absolute; width: 457px; height: 261px; overflow: hidden;
  }
  .card svg.art { position: absolute; inset: 0; width: 100%; height: 100%; }

  /* Front */
  .card-front {
    left: 54px; top: 356px;
    background: var(--paper);
    border: 1px solid var(--red);
    z-index: 2;
  }
  .name {
    position: absolute; left: 193px; top: 86px;
    font-family: "Montserrat", sans-serif; font-weight: 700;
    font-size: 16px; color: #fff; letter-spacing: 0.2px;
  }
  .title {
    position: absolute; left: 350px; top: 96px;
    font-family: "Montserrat", sans-serif; font-size: 9px;
    color: #fff; letter-spacing: 6px;
  }
  .brand {
    position: absolute; left: 330px; top: 44px; width: 120px;
    text-align: center;
    font-family: "Montserrat", sans-serif; font-weight: 600;
    font-size: 8px; letter-spacing: 2px; color: var(--ink);
    line-height: 1.3;
  }
  .brand-mark {
    display: block; width: 14px; height: 14px; margin: 0 auto 6px;
    background: var(--red);
  }
  .contact {
    position: absolute; left: 196px; top: 151px; list-style: none;
    font-size: 10.5px; color: var(--ink);
  }
  .contact li { display: flex; align-items: center; height: 19.5px; }
  .contact svg { width: 10px; height: 10px; margin-right: 10px; }
  .tagline {
    position: absolute; left: 334px; top: 143px;
    font-family: "Montserrat", sans-serif; line-height: 1;
  }
  .tagline .elevated { display: block; font-weight: 800; font-size: 16.5px; color: var(--red); letter-spacing: -0.2px; }
  .tagline .peace { display: block; font-weight: 400; font-size: 31px; color: var(--ink); letter-spacing: -0.5px; margin-top: 1px; }
  .tagline .ofmind { display: block; font-size: 20px; color: var(--red); margin-top: 0; }
  .tagline .ofmind b { font-weight: 800; }

  /* Back */
  .card-back {
    left: 341px; top: 582px;
    background: linear-gradient(135deg, #cc2e30 0%, var(--red) 45%, #a81c22 100%);
    z-index: 1;
  }
  .section-head {
    position: absolute;
    font-family: "Montserrat", sans-serif; font-weight: 700;
    font-size: 16px; color: #fff;
  }
  .head-financial { left: 230px; top: 24px; }
  .head-cyber { left: 230px; top: 143px; }
  .service-list {
    position: absolute; left: 232px; list-style: none;
    font-size: 11px; line-height: 11.6px; color: #fff;
  }
  .service-list li::before { content: "•"; margin-right: 6px; }
  .list-financial { top: 63px; }
  .list-cyber { top: 182px; }
</style>
</head>
<body>
<main class="stage">

  <section class="card card-back" aria-label="Business card back">
    <svg class="art" viewBox="0 0 457 261" aria-hidden="false">
      <defs>
        <linearGradient id="backDecor" x1="0" y1="0" x2="1" y2="1">
          <stop offset="0" stop-color="#ef7a5a" stop-opacity="0.55"/>
          <stop offset="1" stop-color="#c1272d" stop-opacity="0"/>
        </linearGradient>
      </defs>
      <polygon role="img" aria-label="Large faint brand symbol decoration" points="0,0 230,0 85,261 0,261" fill="url(#backDecor)"/>
      <polygon points="225,16 425,16 425,50 213,50" fill="var(--band-light)"/>
      <polygon points="157,137 423,137 423,170 145,170" fill="var(--band-light)"/>
    </svg>
    <h2 class="section-head head-financial">FINANCIAL</h2>
    <ul class="service-list list-financial">
      <li>card processing</li>
      <li>website design</li>
      <li>hosting</li>
      <li>maintenance</li>
      <li>VoIP phone systems</li>
    </ul>
    <h2 class="section-head head-cyber">CYBER SECURITY</h2>
    <ul class="service-list list-cyber">
      <li>network vulnerability scan</li>
      <li>dark web scan</li>
      <li>anti-ransomeware</li>
      <li>malware software</li>
      <li>and image-level backups</li>
    </ul>
  </section>

  <section class="card card-front" aria-label="Business card front">
    <svg class="art" viewBox="0 0 457 261">
      <defs>
        <linearGradient id="frontDecor" x1="0" y1="0" x2="1" y2="1">
          <stop offset="0" stop-color="var(--red-deep)"/>
          <stop offset="0.55" stop-color="var(--red-bright)"/>
          <stop offset="1" stop-color="#b3161c"/>
        </linearGradient>
        <linearGradient id="nameBand" x1="0" y1="0" x2="1" y2="0">
          <stop offset="0" stop-color="#a3141a"/>
          <stop offset="1" stop-color="var(--red)"/>
        </linearGradient>
      </defs>
      <polygon role="img" aria-label="Large brand symbol decoration" points="0,0 230,0 82,261 0,261" fill="url(#frontDecor)"/>
      <polygon points="185,80 330,80 318,113 166,113" fill="url(#nameBand)"/>
      <polygon points="331,92 435,92 435,113 322,113" fill="var(--ink)"/>
    </svg>
    <div class="name">YOUR NAME</div>
    <div class="title">TITLE</div>
    <div class="brand"><span class="brand-mark"></span>BRIGHTMOOR PARTNERS</div>
    <ul class="contact">
      <li><svg viewBox="0 0 10 10"><rect x="2.5" y="0.5" width="5" height="9" rx="0.8" fill="none" stroke="var(--red)" stroke-width="1"/></svg>Phone</li>
      <li><svg viewBox="0 0 10 10"><rect x="0.5" y="2" width="9" height="6.5" fill="var(--red)"/><path d="M0.5 2 L5 5.8 L9.5 2" fill="none" stroke="#fff" stroke-width="0.9"/></svg>email</li>
      <li><svg viewBox="0 0 10 10"><path d="M5 9.5 C2.5 6.5 1.8 5 1.8 3.6 A3.2 3.2 0 0 1 8.2 3.6 C8.2 5 7.5 6.5 5 9.5Z" fill="var(--red)"/><circle cx="5" cy="3.6" r="1.2" fill="#fff"/></svg>Address</li>
    </ul>
    <p class="tagline">
      <span class="elevated">ELEVATED</span>
      <span class="peace">PEACE</span>
      <span class="ofmind">OF <b>MIND</b></span>
    </p>
  </section>

</main>
</body>
</html>
```